Pop-up Banner

Would like a design for a pop-up 85 x 206cm banner for a trade show. (from norla press)
We would like "our logo" (brightwave holdings) - then the tagline - "Your Trusted Partner in Data-Driven Decisions"
*Supporting Bullets*
Unified data, analytics & AI
Trusted insights, faster outcomes
Real-time intelligence at scale
Enterprise-ready, secure solutions
Clarity from data complexity
trusted by...some company logos
Partners with : partner logo
Our Colours: #FFA300, #3D4176, #FDD16E, #F87C57, #A68118, #1C2F36

```html
<!DOCTYPE html>
<html lang="en">
<head>
<meta charset="utf-8">
<title>Brightwave Holdings – Pop-up Banner</title>
<link rel="stylesheet" href="https://fonts.googleapis.com/css2?family=Poppins:wght@300;400;600&family=Sora:wght@600&family=Comfortaa:wght@400&display=swap">
<style>
  :root {
    --navy-deep: #121526;
    --navy: #1a1d33;
    --indigo: #3D4176;
    --gold: #FDD16E;
    --gold-dark: #A68118;
    --orange: #FFA300;
    --coral: #F87C57;
    --white: #ffffff;
    --ink: #1C2F36;
    --stage: #ffffff;
  }
  * { margin: 0; padding: 0; box-sizing: border-box; }
  html, body { width: 1200px; height: 1042px; overflow: hidden; background: var(--stage); }
  .banner {
    position: absolute; left: 393px; top: 21px; width: 414px; height: 1000px;
    overflow: hidden; color: var(--white);
    font-family: "Comfortaa", "Poppins", sans-serif;
    background:
      radial-gradient(ellipse 70% 22% at 50% 100%, rgba(214,172,88,.95), rgba(166,129,24,.35) 55%, transparent 100%),
      linear-gradient(180deg, var(--navy-deep) 0%, var(--navy) 55%, #2a2628 82%, #6b5630 100%);
  }
  .banner__wave {
    position: absolute; inset: 0; pointer-events: none;
  }
  .brand {
    position: absolute; top: 78px; left: 0; width: 100%;
    display: flex; justify-content: center; align-items: center; gap: 14px;
  }
  .brand__dot { width: 58px; height: 58px; border-radius: 50%; border: 9px solid var(--gold); }
  .brand__name {
    font-family: "Poppins", sans-serif; font-weight: 600; color: var(--gold);
    font-size: 24px; line-height: 30px; letter-spacing: 1.5px;
  }
  .tagline {
    position: absolute; top: 218px; left: 0; width: 100%; text-align: center;
    font-family: "Sora", "Poppins", sans-serif; font-weight: 600;
    font-size: 48px; line-height: 58px; letter-spacing: -1px;
  }
  .tagline__gold { color: var(--gold); }
  .tagline__coral { color: var(--coral); }
  .benefit {
    position: absolute; display: flex; align-items: center; gap: 8px;
    font-size: 15px; line-height: 19px; letter-spacing: -.3px;
  }
  .benefit svg { width: 26px; height: 26px; flex: none; fill: none; stroke: var(--gold); stroke-width: 1.4; stroke-linecap: round; stroke-linejoin: round; }
  .benefit--left { left: 72px; }
  .benefit--right { left: 174px; }
  .section-label {
    position: absolute; left: 0; width: 100%; text-align: center;
    color: var(--gold); font-size: 18px;
  }
  .partners {
    position: absolute; top: 854px; left: 30px; right: 22px; height: 24px;
    display: flex; justify-content: space-between; align-items: center;
    font-family: "Poppins", sans-serif; font-weight: 600; font-size: 14px; color: var(--white);
  }
  .partners span + span { border-left: 1px solid rgba(255,255,255,.5); padding-left: 8px; }
  .partner__mark { display: inline-block; width: 10px; height: 10px; background: var(--gold); margin-right: 5px; }
  .clients {
    position: absolute; top: 934px; left: 32px; width: 359px; height: 37px; background: var(--white);
    display: flex; justify-content: space-around; align-items: center;
    font-family: "Poppins", sans-serif; font-weight: 600; font-size: 15px; color: var(--ink);
  }
</style>
</head>
<body>
<main class="banner">
  <svg class="banner__wave" viewBox="0 0 414 1000" preserveAspectRatio="none" aria-hidden="true">
    <defs>
      <linearGradient id="waveTone" x1="0" y1="0" x2="1" y2="1">
        <stop offset="0" stop-color="#3D4176" stop-opacity=".0"/>
        <stop offset=".5" stop-color="#3D4176" stop-opacity=".45"/>
        <stop offset="1" stop-color="#1e3a5c" stop-opacity=".15"/>
      </linearGradient>
    </defs>
    <path d="M414 160 C380 260 320 320 320 420 C320 560 200 620 80 660 C20 690 20 780 60 860 L0 860 L0 640 C120 600 230 560 250 440 C270 320 380 260 414 120 Z" fill="url(#waveTone)"/>
  </svg>

  <header class="brand">
    <span class="brand__dot"></span>
    <span class="brand__name">BRIGHTWAVE<br>HOLDINGS</span>
  </header>

  <h1 class="tagline">
    Your <span class="tagline__gold">Trusted</span><br>
    Partner in<br>
    <span class="tagline__coral">Data-Driven</span><br>
    Decisions
  </h1>

  <div class="benefit benefit--left" style="top:606px;top:492px">
    <svg viewBox="0 0 26 26"><path d="M2 23h22M4 23v-6h3v6M9 23v-9h3v9M14 23v-7h3v7M19 23v-12h3v12M5 12l6-4 5 3 6-7"/></svg>
    <span>Unified data,<br>analytics &amp; AI</span>
  </div>
  <div class="benefit benefit--right" style="top:550px">
    <svg viewBox="0 0 26 26"><path d="M13 3a8 8 0 0 0-5 14v3h10v-3a8 8 0 0 0-5-14zM9 23h8M10 13l3-3 2 2 2-3"/></svg>
    <span>Trusted insights,<br>faster outcomes</span>
  </div>
  <div class="benefit benefit--left" style="top:605px">
    <svg viewBox="0 0 26 26"><circle cx="13" cy="13" r="7"/><path d="M13 6v14M9 10h4M13 15h4M13 1v2M13 23v2M1 13h2M23 13h2M4.5 4.5l1.5 1.5M20 20l1.5 1.5M4.5 21.5l1.5-1.5M20 6l1.5-1.5"/></svg>
    <span>Real-time<br>intelligence at scale</span>
  </div>
  <div class="benefit benefit--right" style="top:667px">
    <svg viewBox="0 0 26 26"><path d="M13 2l9 4v7c0 5-4 9-9 11-5-2-9-6-9-11V6z"/><rect x="9.5" y="12" width="7" height="6" rx="1"/><path d="M11 12v-2a2 2 0 0 1 4 0v2"/></svg>
    <span>Enterprise-ready,<br>secure solutions</span>
  </div>
  <div class="benefit benefit--left" style="top:726px">
    <svg viewBox="0 0 26 26"><rect x="10" y="10" width="6" height="6"/><path d="M10 13H4M16 13h6M13 10V4M13 16v6M10 10L6 6M16 16l4 4M16 10l4-4M10 16l-4 4"/><circle cx="3" cy="13" r="1.4"/><circle cx="23" cy="13" r="1.4"/><circle cx="13" cy="3" r="1.4"/><circle cx="5" cy="21" r="1.4"/><circle cx="21" cy="5" r="1.4"/></svg>
    <span>Clarity from<br>data complexity</span>
  </div>

  <p class="section-label" style="top:812px">Partners With</p>
  <div class="partners">
    <span><i class="partner__mark"></i>Northlane</span>
    <span>Veranth</span>
    <span>Quorix</span>
    <span>clearmetric</span>
  </div>

  <p class="section-label" style="top:896px">Trusted By</p>
  <div class="clients">
    <span>Orvel</span>
    <span>Tavora</span>
    <span>Plinth</span>
    <span>Marrow</span>
  </div>
</main>
</body>
</html>
```